Professional Modern Website Design

We are a premium IT services provider to the financial industry based in London. Our company is called Veltra our current holding page is www.veltra-example.co.uk. We require a new website to match our new corporate identity. This project is for the design phase only. Development will be handled in-house. I have attached examples of wire frames we have developed (although open to suggestions for improvement) Our brand document that should demonstrate current brand, inc how we communicate to potential clients and finally mostly completed web-content.
We are looking for designers that can create something that sets us apart from our competitors.
Target Market(s)
IT Decision makers in Finance companies such as; hedge funds, private investment banks etc
Industry/Entity Type
Financial
Number of Pages Required
5+ page
Requirements
Must have
- hexagon elements in the design, unique design.
Nice to have
- Blog and social media feeds
Should not have
- Should not resemble a downloaded template

```html
<!DOCTYPE html>
<html lang="en">
<head>
<meta charset="utf-8">
<title>Veltra — Services</title>
<link href="https://fonts.googleapis.com/css2?family=Arimo:wght@400;700&display=swap" rel="stylesheet">
<style>
  :root {
    --backdrop: #d6d7d9;
    --page: #ffffff;
    --accent: #ef6a32;
    --accent-soft: #f39a5c;
    --ink: #4a4a4a;
    --muted: #8a8a8a;
    --nav: #7a7a7a;
    --panel: rgba(40, 40, 40, 0.82);
    --footer-deep: #1c1d1f;
  }
  * { box-sizing: border-box; margin: 0; padding: 0; }
  html, body { width: 939px; height: 1200px; overflow: hidden; }
  body {
    background: var(--backdrop);
    font-family: "Arimo", Helvetica, Arial, sans-serif;
    color: var(--ink);
    position: relative;
  }
  .site {
    position: absolute;
    left: 144px; top: 91px;
    width: 651px; height: 1018px;
    background: var(--page);
    overflow: hidden;
  }
  /* header */
  .site-header { position: relative; height: 76px; }
  .brand {
    position: absolute; left: 38px; top: 24px;
    display: flex; align-items: center; gap: 7px;
    color: var(--accent); font-weight: 700; font-size: 17px; letter-spacing: 0.5px;
  }
  .brand-mark { width: 12px; height: 12px; background: var(--accent); }
  .main-nav {
    position: absolute; right: 26px; top: 32px;
    display: flex; gap: 24px;
  }
  .main-nav a {
    font-size: 8.5px; color: var(--nav); text-decoration: none; letter-spacing: 0.2px;
    position: relative; padding-bottom: 10px;
  }
  .main-nav a.is-active::after {
    content: ""; position: absolute; left: 0; right: 0; bottom: 0;
    height: 2px; background: var(--accent);
  }
  /* hero */
  .hero { position: relative; height: 357px; }
  .hero-photo {
    position: absolute; inset: 0;
    background:
      radial-gradient(ellipse at 60% 45%, rgba(255,240,220,0.55) 0%, rgba(255,240,220,0) 18%),
      linear-gradient(180deg, #1e2a3e 0%, #2b3141 35%, #6f6e68 62%, #a9a69d 85%, #8f8c84 100%);
  }
  .hero-panel {
    position: absolute; left: 28px; top: 104px;
    width: 271px; height: 145px;
    background: var(--panel);
    padding: 22px 26px 0 26px;
  }
  .hero-title { color: #fff; font-weight: 700; font-size: 8.8px; margin-bottom: 13px; white-space: nowrap; }
  .hero-quote {
    border-left: 2px solid var(--accent);
    padding-left: 11px;
    color: #d8d8d8; font-size: 8.5px; line-height: 14.5px;
  }
  .slider-dots { position: absolute; left: 283px; top: 330px; display: flex; gap: 6px; }
  .slider-dots span { width: 22px; height: 2px; background: var(--accent-soft); opacity: 0.6; }
  .slider-dots span.is-current { opacity: 1; background: var(--accent); }
  /* audience */
  .audience { position: relative; height: 382px; text-align: center; }
  .audience-title { padding-top: 33px; color: var(--accent); font-size: 17px; font-weight: 700; }
  .audience-lede { margin-top: 9px; font-size: 7.6px; line-height: 15px; color: var(--muted); }
  .roles { position: absolute; top: 125px; left: 24px; display: flex; gap: 30px; }
  .role { width: 122px; display: flex; flex-direction: column; align-items: center; }
  .role svg { width: 64px; height: 70px; }
  .role-title { margin-top: 22px; color: var(--accent); font-weight: 700; font-size: 8px; white-space: nowrap; }
  .role-copy { margin-top: 10px; width: 104px; font-size: 6.7px; line-height: 10.9px; color: var(--muted); }
  /* footer */
  .site-footer {
    position: absolute; left: 0; right: 0; top: 815px; height: 203px;
    background: linear-gradient(180deg, #2a2c30 0%, var(--footer-deep) 60%, #2b2624 100%);
  }
  .footer-brand {
    position: absolute; left: 0; right: 0; top: 72px;
    text-align: center; color: var(--accent); font-weight: 700; font-size: 22px;
  }
  .footer-links {
    position: absolute; left: 0; right: 0; top: 138px;
    display: flex; justify-content: center; align-items: center; gap: 9px;
    color: #fff; font-size: 8px; font-weight: 700;
  }
  .footer-links .dot { width: 7px; height: 7px; border-radius: 50%; background: #fff; }
</style>
</head>
<body>
  <div class="site">
    <header class="site-header">
      <div class="brand"><span class="brand-mark"></span>Veltra</div>
      <nav class="main-nav">
        <a href="#">ABOUT</a>
        <a href="#" class="is-active">SERVICES</a>
        <a href="#">PARTNERS</a>
        <a href="#">CLIENTS</a>
        <a href="#">CONTACT</a>
      </nav>
    </header>

    <section class="hero">
      <div class="hero-photo" role="img" aria-label="City road at night curving past lit office towers"></div>
      <div class="hero-panel">
        <h1 class="hero-title">You need integration. We're always there with you</h1>
        <p class="hero-quote">Veltra is one of the leading systems integrators to the world's finance sector. We are an extension of your business and our services portfolio has been built so you always have access to a complete partner.</p>
      </div>
      <div class="slider-dots"><span></span><span></span><span class="is-current"></span></div>
    </section>

    <section class="audience">
      <h2 class="audience-title">Who Are You?</h2>
      <p class="audience-lede">If you're part of a financial organisation, we have the power to help everyone work more<br>Efficiently, Productively and Profitably</p>
      <div class="roles">
        <article class="role">
          <svg viewBox="0 0 64 70" role="img" aria-label="Portrait of senior executives"><polygon points="32,1 63,18 63,52 32,69 1,52 1,18" fill="#b9b3ad" stroke="#ef6a32" stroke-width="1"/></svg>
          <h3 class="role-title">Senior Hedge Fund Manager/CEO</h3>
          <p class="role-copy">You need to develop and implement strategies for business growth, while ensuring profitability. You're aware your biggest asset is your staff and a happy workforce is a productive one. Security is a key concern in a changing always-on world and you need to be compliant, but you don't want to overspend. Veltra can help you find the best solutions to help your business grow at the speed you want it to</p>
        </article>
        <article class="role">
          <svg viewBox="0 0 64 70" role="img" aria-label="Portrait of a finance director"><polygon points="32,1 63,18 63,52 32,69 1,52 1,18" fill="#7d8088" stroke="#ef6a32" stroke-width="1"/></svg>
          <h3 class="role-title">CFO</h3>
          <p class="role-copy">Your key responsibility is to obtain the maximum ROI from products and services. You understand investment opportunities, providing they return higher efficiencies and revenues. You are concerned more with long-term spending versus short-term and how you can get the most value out of a proposition. Veltra can advise how to boost ROI by streamlining your business to</p>
        </article>
        <article class="role">
          <svg viewBox="0 0 64 70" role="img" aria-label="Portrait of an IT manager"><polygon points="32,1 63,18 63,52 32,69 1,52 1,18" fill="#6e6e6e" stroke="#ef6a32" stroke-width="1"/></svg>
          <h3 class="role-title">IT Manager/CTO</h3>
          <p class="role-copy">Integration with partners and services is your key concern. You want to make sure any IT system you implement will work with the whole infrastructure of your company. You don't want your team to waste valuable time dealing with things that don't matter. Veltra provides the whole picture to ensure your company is ready for the next generation of IT.</p>
        </article>
        <article class="role">
          <svg viewBox="0 0 64 70" role="img" aria-label="Portrait of an employee"><polygon points="32,1 63,18 63,52 32,69 1,52 1,18" fill="#6f6a66" stroke="#ef6a32" stroke-width="1"/></svg>
          <h3 class="role-title">Employees</h3>
          <p class="role-copy">You're working hard, but not getting anywhere fast. You want the tools to make your job easier so you can spend more time thinking about what you're doing rather than how you're doing it. You shouldn't have to think about the technology you're using, because it should just work. Veltra can help you get back on track everyday.</p>
        </article>
      </div>
    </section>

    <footer class="site-footer" role="img" aria-label="Dim London street with buses and office towers behind the footer">
      <div class="footer-brand">Veltra</div>
      <div class="footer-links"><span class="dot"></span><span class="dot"></span><span class="dot"></span><span>BLOG</span></div>
    </footer>
  </div>
</body>
</html>
```